Header and footer for report

We would like a header and footer for our building management reports that incorporate a modern city skyline and our logo.

As well as update our other stationery.

```html
<!DOCTYPE html>
<html lang="en">
<head>
<meta charset="utf-8">
<title>Kestra Group – Stationery Set</title>
<link href="https://fonts.googleapis.com/css2?family=Exo+2:wght@600&family=Roboto+Condensed:wght@400;700&display=swap" rel="stylesheet">
<style>
  :root {
    --canvas: #d3d4d6;
    --paper: #ffffff;
    --brand-blue: #1b63aa;
    --brand-blue-light: #2f72bf;
    --brand-blue-deep: #164f8c;
    --deep-teal: #06333b;
    --swoosh-grey: #d9d9da;
    --skyline-grey: #e6e6e7;
    --text-grey: #9c9c9c;
    --heading-grey: #767676;
    --contact-grey: #555555;
  }
  * { box-sizing: border-box; margin: 0; padding: 0; }
  html, body { width: 1200px; height: 1192px; overflow: hidden; }
  body {
    background: var(--canvas);
    position: relative;
    font-family: "Roboto Condensed", sans-serif;
  }
  address { font-style: normal; }
  .sheet {
    position: absolute;
    background: var(--paper);
    overflow: hidden;
    box-shadow: 2px 3px 6px rgba(0,0,0,0.18);
  }
  .sheet > svg { position: absolute; left: 0; top: 0; }
  .wordmark {
    position: absolute;
    font-family: "Exo 2", sans-serif;
    font-weight: 600;
    color: var(--brand-blue);
    line-height: 1;
    white-space: nowrap;
    letter-spacing: 0.2px;
  }

  /* Letterheads */
  .letterhead { width: 485px; height: 680px; top: 60px; }
  .letterhead--contact { left: 83px; }
  .letterhead--plain { left: 628px; }
  .letterhead .wordmark { font-size: 21px; top: 96px; }
  .letterhead--contact .wordmark { left: 54px; }
  .letterhead--plain .wordmark { left: 304px; top: 101px; }

  .sender-block {
    position: absolute; left: 316px; top: 60px; width: 108px;
    font-size: 5.2px; line-height: 6.4px; color: var(--text-grey);
  }
  .sender-block strong { color: var(--heading-grey); display: block; margin-bottom: 3px; font-size: 5.6px; }

  .report-body {
    position: absolute; left: 57px; top: 180px; width: 377px;
    color: var(--text-grey);
  }
  .report-body h2 {
    font-size: 7.2px; line-height: 8px; font-weight: 700;
    color: var(--heading-grey); margin-bottom: 8px;
  }
  .report-body p {
    font-size: 6.1px; line-height: 9.5px; text-align: justify; margin-bottom: 9px;
  }
  .report-body p + h2 { margin-top: 13px; }

  .footer-contacts {
    position: absolute; left: 0; top: 604px; width: 485px; height: 40px;
  }
  .contact-item {
    position: absolute; top: 0; width: 120px; padding-left: 20px;
    color: #ffffff; font-size: 6px; line-height: 7.6px;
  }
  .contact-item svg { position: absolute; left: 3px; top: 1px; }
  .contact-item strong { display: block; font-size: 6.4px; margin-bottom: 4px; }
  .contact-item--web { left: 73px; }
  .contact-item--office { left: 201px; }
  .contact-item--phone { left: 333px; }

  /* Envelope */
  .envelope {
    position: absolute; left: 80px; top: 814px; width: 505px; height: 308px;
    filter: drop-shadow(2px 3px 4px rgba(0,0,0,0.18));
  }
  .envelope svg { position: absolute; left: 0; top: 0; }
  .envelope .wordmark { font-size: 21px; left: 325px; top: 140px; }

  /* Business cards */
  .card { width: 280px; height: 165px; }
  .card--front { left: 732px; top: 775px; }
  .card--back { left: 730px; top: 960px; }
  .card--front .wordmark { font-size: 19px; left: 76px; top: 104px; }
  .card--back .wordmark { font-size: 15.5px; right: 21px; top: 66px; }
  .card-contact {
    position: absolute; right: 21px; top: 97px; text-align: right;
    font-size: 9.6px; line-height: 15.4px; color: var(--contact-grey);
    letter-spacing: -0.2px; white-space: nowrap;
  }
</style>
</head>
<body>

  <!-- Letterhead with footer contacts -->
  <section class="sheet letterhead letterhead--contact">
    <svg width="485" height="680" viewBox="0 0 485 680">
      <defs>
        <linearGradient id="skylineBlue" x1="0" y1="0" x2="0" y2="1">
          <stop offset="0" stop-color="#1e5f9f" stop-opacity="0"/>
          <stop offset="0.5" stop-color="#1a5690" stop-opacity="0.6"/>
          <stop offset="1" stop-color="#184f86"/>
        </linearGradient>
      </defs>
      <path d="M105 498 Q 260 575 485 520 L485 556 Q 270 575 105 498 Z" fill="var(--swoosh-grey)"/>
      <path d="M0 490 Q 200 590 485 576 L485 680 L0 680 Z" fill="var(--brand-blue)"/>
      <path d="M0 456 Q 200 582 485 564 L485 578 Q 200 592 0 464 Z" fill="var(--deep-teal)"/>
      <rect x="0" y="588" width="485" height="92" fill="url(#skylineBlue)" role="img" aria-label="City skyline silhouette with harbour bridge"/>
    </svg>

    <div class="wordmark">KESTRA GROUP</div>

    <address class="sender-block">
      <strong>Building Management Division</strong>
      12 Harbour Street, Level 4<br>
      Port City 2000<br>
      Phone +1 555 014 277<br>
      office@kestragroup.com
    </address>

    <article class="report-body">
      <h2>Quarterly Building Management Report Summary</h2>
      <p>This report sets out the condition of the managed buildings over the past quarter, covering scheduled maintenance, tenant requests, energy use and safety inspections. All major plant items were serviced on time and no critical faults were recorded. Lift availability remained above target across every site, while water use fell compared with the same period last year. Minor repairs to facades and car park lighting were completed within budget.</p>
      <p>Tenant satisfaction scores improved slightly, with most feedback relating to cleaning standards and response times. A revised cleaning schedule begins next month at all sites.</p>
      <h2>Planned Works and Budget Outlook for Next Quarter</h2>
      <p>Next quarter the focus moves to roof membrane renewal at two sites, replacement of ageing boiler controls and an upgrade of the access card system. Contractors have been appointed through a competitive tender and works are programmed to limit disruption to tenants. Budget forecasts remain in line with the annual plan, with a small contingency held for unexpected repairs. Fire door surveys will be repeated in all stairwells, and any defects found will be corrected before the end of the period. Energy monitoring will be extended to common areas so that lighting and ventilation can be tuned to actual occupancy. We will also review cleaning and security contracts, seek tenant views on shared spaces, and report progress in the next edition of this summary.</p>
    </article>

    <footer class="footer-contacts">
      <div class="contact-item contact-item--web">
        <svg width="13" height="13" viewBox="0 0 13 13"><circle cx="6.5" cy="6.5" r="6.5" fill="#fff"/><circle cx="6.5" cy="6.5" r="4" fill="none" stroke="var(--brand-blue)" stroke-width="1"/><path d="M2.5 6.5h8M6.5 2.5v8" stroke="var(--brand-blue)" stroke-width="0.8"/></svg>
        <strong>Web</strong>www.kestragroup.com<br>Tenant portal
      </div>
      <div class="contact-item contact-item--office">
        <svg width="13" height="13" viewBox="0 0 13 13"><circle cx="6.5" cy="6.5" r="6.5" fill="#fff"/><path d="M3 6.8 L6.5 3.5 L10 6.8 L9 6.8 L9 9.8 L4 9.8 L4 6.8 Z" fill="var(--brand-blue)"/></svg>
        <strong>Office</strong>12 Harbour Street<br>Port City 2000
      </div>
      <div class="contact-item contact-item--phone">
        <svg width="13" height="13" viewBox="0 0 13 13"><circle cx="6.5" cy="6.5" r="6.5" fill="#fff"/><path d="M4 3.5 L5.5 3.3 L6.2 5.2 L5.3 6 Q6 7.3 7 8 L7.8 7.1 L9.7 7.8 L9.5 9.3 Q6.5 9.6 4.8 7.8 Q3.3 6 4 3.5 Z" fill="var(--brand-blue)"/></svg>
        <strong>Phone</strong>+1 555 014 277<br>Mon–Fri 8–6
      </div>
    </footer>
  </section>

  <!-- Letterhead, continuation page -->
  <section class="sheet letterhead letterhead--plain">
    <svg width="485" height="680" viewBox="0 0 485 680">
      <defs>
        <linearGradient id="skylineGrey" x1="0" y1="0" x2="0" y2="1">
          <stop offset="0" stop-color="var(--skyline-grey)" stop-opacity="0"/>
          <stop offset="0.35" stop-color="var(--skyline-grey)" stop-opacity="0.8"/>
          <stop offset="1" stop-color="var(--skyline-grey)"/>
        </linearGradient>
      </defs>
      <rect x="40" y="530" width="445" height="135" fill="url(#skylineGrey)" role="img" aria-label="Faint city skyline with harbour bridge"/>
      <path d="M0 579 Q 140 670 485 667 L485 680 L0 680 Z" fill="var(--brand-blue)"/>
      <path d="M0 546 Q 150 650 485 652 L485 667 Q 150 664 0 556 Z" fill="var(--deep-teal)"/>
    </svg>

    <div class="wordmark">KESTRA GROUP</div>

    <article class="report-body">
      <h2>Quarterly Building Management Report Summary</h2>
      <p>This report sets out the condition of the managed buildings over the past quarter, covering scheduled maintenance, tenant requests, energy use and safety inspections. All major plant items were serviced on time and no critical faults were recorded. Lift availability remained above target across every site, while water use fell compared with the same period last year. Minor repairs to facades and car park lighting were completed within budget.</p>
      <p>Tenant satisfaction scores improved slightly, with most feedback relating to cleaning standards and response times. A revised cleaning schedule begins next month at all sites.</p>
      <h2>Planned Works and Budget Outlook for Next Quarter</h2>
      <p>Next quarter the focus moves to roof membrane renewal at two sites, replacement of ageing boiler controls and an upgrade of the access card system. Contractors have been appointed through a competitive tender and works are programmed to limit disruption to tenants. Budget forecasts remain in line with the annual plan, with a small contingency held for unexpected repairs. Fire door surveys will be repeated in all stairwells, and any defects found will be corrected before the end of the period. Energy monitoring will be extended to common areas so that lighting and ventilation can be tuned to actual occupancy. We will also review cleaning and security contracts, seek tenant views on shared spaces, and report progress in the next edition of this summary.</p>
    </article>
  </section>

  <!-- Envelope -->
  <section class="envelope">
    <svg width="505" height="308" viewBox="0 0 505 308">
      <defs>
        <clipPath id="envelopeBody"><rect x="0" y="55" width="505" height="253"/></clipPath>
        <linearGradient id="envelopeSkyline" x1="0" y1="0" x2="0" y2="1">
          <stop offset="0" stop-color="#184f86" stop-opacity="0.3"/>
          <stop offset="1" stop-color="#174a7e"/>
        </linearGradient>
      </defs>
      <path d="M13 0 L491 0 Q496 0 497 5 L505 56 L0 56 L8 5 Q9 0 13 0 Z" fill="var(--deep-teal)"/>
      <rect x="0" y="55" width="505" height="253" fill="var(--paper)"/>
      <g clip-path="url(#envelopeBody)">
        <path d="M108 144 Q 270 218 505 167 L505 206 Q 280 220 108 144 Z" fill="var(--swoosh-grey)"/>
        <path d="M0 137 Q 200 232 505 229 L505 308 L0 308 Z" fill="var(--brand-blue)"/>
        <path d="M0 104 Q 200 225 505 216 L505 229 Q 200 236 0 114 Z" fill="var(--deep-teal)"/>
        <rect x="0" y="236" width="505" height="72" fill="url(#envelopeSkyline)" role="img" aria-label="City skyline silhouette with harbour bridge"/>
      </g>
    </svg>
    <div class="wordmark">KESTRA GROUP</div>
  </section>

  <!-- Business card, front -->
  <section class="sheet card card--front">
    <svg width="280" height="165" viewBox="0 0 280 165">
      <defs>
        <linearGradient id="cardSkyline" x1="0" y1="0" x2="0" y2="1">
          <stop offset="0" stop-color="var(--skyline-grey)" stop-opacity="0"/>
          <stop offset="0.4" stop-color="var(--skyline-grey)" stop-opacity="0.7"/>
          <stop offset="1" stop-color="var(--skyline-grey)"/>
        </linearGradient>
      </defs>
      <rect x="0" y="56" width="280" height="109" fill="url(#cardSkyline)" role="img" aria-label="Faint city skyline with harbour bridge"/>
    </svg>
    <div class="wordmark">KESTRA GROUP</div>
  </section>

  <!-- Business card, back -->
  <section class="sheet card card--back">
    <svg width="280" height="165" viewBox="0 0 280 165">
      <path d="M0 0 L154 0 Q 80 60 58 165 L0 165 Z" fill="var(--brand-blue)"/>
      <path d="M0 0 L110 0 Q 40 28 0 80 Z" fill="var(--brand-blue-light)"/>
      <path d="M4 165 Q 30 72 122 22 Q 52 80 16 165 Z" fill="var(--deep-teal)"/>
      <path d="M64 165 Q 74 92 122 50 Q 92 100 80 165 Z" fill="var(--swoosh-grey)"/>
    </svg>
    <div class="wordmark">KESTRA GROUP</div>
    <address class="card-contact">
      Phone: +1 555 014 277<br>
      Adress: Port City, 12 Harbour Street<br>
      Mail: office@kestragroup.com
    </address>
  </section>

</body>
</html>
```